Brand new letterhead, business card, email signature etc.

We are a financial company in London, UK. Our website is www.quorvane.com. We're wanting a complete remodel of the company colours, letter head, business cards, email signatures, etc. Looking to keep the same font for the company name. I have upload a colour palette that we want to work with. We're looking for company letterhead for outgoing letters/ correspondence, letterhead for internal documentation, email signatures, e-letters. etc. Ultimately we will redesign the entire website also. It is important that our clients get a strong, secure, warm, trustworthy, solid feeling and first impression.
Updates

Designs look the same

Target Market(s)

Institutional investors, (ultra) high net worth individuals

Industry/Entity Type

Finance, Invesments banking.

Font styles to use
Other font styles liked:
• Current font is "Champagne & Limousines"

Requirements
Must have
• Must use the colours provided on the PDF uploaded to the portal. The purple = main colour. The red = accent colour.
Nice to have
• Nice to use same font as now for the company name "Marlowin". Font is "Champagne & Limousines". Nice to have some reference to the old logo flower, but only subtle.
Should not have
• Do not use the colour red from our website. Use the colours provided on the colour palette PDF that I uploaded in the portal.

```html
<!DOCTYPE html>
<html lang="en">
<head>
<meta charset="utf-8">
<title>Marlowin Letterhead</title>
<link href="https://fonts.googleapis.com/css2?family=Didact+Gothic&family=Quicksand:wght@400&display=swap" rel="stylesheet">
<style>
  :root {
    --backdrop: #e9e6e4;
    --paper: #ffffff;
    --accent-red: #e2391b;
    --sand: #ddd3c2;
    --ink: #1c1a1a;
    --ink-soft: #2b2b2b;
    --footer-grey: #8a8a8a;
  }
  * { margin: 0; padding: 0; box-sizing: border-box; }
  html, body {
    width: 1191px;
    height: 1200px;
    overflow: hidden;
    background: var(--backdrop);
  }
  .letterhead {
    position: absolute;
    left: 199px;
    top: 40px;
    width: 792px;
    height: 1121px;
    background: var(--paper);
    box-shadow: 0 6px 24px rgba(0, 0, 0, 0.12);
    font-family: "Didact Gothic", "Century Gothic", sans-serif;
    color: var(--ink-soft);
  }
  .brand {
    position: absolute;
    left: 140px;
    top: 53px;
    display: flex;
    align-items: center;
    gap: 12px;
  }
  .brand-square {
    width: 54px;
    height: 54px;
    border: 1.5px solid var(--ink-soft);
  }
  .brand-name {
    font-family: "Quicksand", "Didact Gothic", sans-serif;
    font-size: 33px;
    letter-spacing: 4px;
    color: var(--ink-soft);
    line-height: 1;
  }
  .header-rules { position: absolute; left: 0; top: 0; }
  .letter-title {
    position: absolute;
    left: 135px;
    top: 294px;
    font-size: 18.5px;
    font-weight: 400;
    letter-spacing: 0.4px;
    color: var(--ink);
  }
  .letter-body {
    position: absolute;
    left: 135px;
    top: 345px;
    width: 515px;
    font-size: 12.6px;
    line-height: 17.3px;
    letter-spacing: 0.15px;
    color: var(--ink);
  }
  .letter-body p + p { margin-top: 17.3px; }
  .footer-rule {
    position: absolute;
    left: 137px;
    top: 1025px;
    width: 518px;
    height: 4px;
    border-radius: 2px;
    background: var(--accent-red);
  }
  .footer-address {
    position: absolute;
    left: 0;
    top: 1043px;
    width: 792px;
    text-align: center;
    font-size: 8px;
    line-height: 11px;
    color: var(--footer-grey);
  }
  .footer-address .web { margin-bottom: 5px; }
</style>
</head>
<body>
  <main class="letterhead">
    <header class="brand">
      <span class="brand-square"></span>
      <span class="brand-name">MARLOWIN</span>
    </header>

    <svg class="header-rules" width="792" height="160" viewBox="0 0 792 160" aria-hidden="true">
      <line x1="139" y1="123" x2="653" y2="123" stroke="var(--accent-red)" stroke-width="4.5" stroke-linecap="round"/>
      <line x1="139" y1="132" x2="623" y2="132" stroke="var(--sand)" stroke-width="3" stroke-linecap="round"/>
      <circle cx="632" cy="132" r="1.5" fill="var(--sand)"/>
      <circle cx="641" cy="132" r="1.5" fill="var(--sand)"/>
      <line x1="139" y1="139" x2="583" y2="139" stroke="var(--ink)" stroke-width="2.5" stroke-linecap="round"/>
      <circle cx="589" cy="139" r="2" fill="var(--ink)"/>
    </svg>

    <h1 class="letter-title">Lorem ipsum dolor sit</h1>

    <section class="letter-body">
      <p>Lorem ipsum dolor sit amet, consectetuer adipiscing elit, sed diam nonummy nibh euismod tincidunt ut laoreet dolore magna aliquam erat volutpat. Ut wisi enim ad minim veniam, quis nostrud exerci tation ullamcorper suscipit lobortis nislvu feugiat nulla facilisis at vero eros et accumsan et iusto odio dignissim qui blandit praesent luptatum zzril delenit augue duis dolore te feugait nulla facilisi.<br>Lorem ipsum dolor sit amet, cons ectetuer adipiscing elit, sed diam nonummy nibh euismod tincidunt ut laoreet dolore magna aliquam erat volutpat. Ut wisi enim ad minim veniam, quis nostrud exerci tation ullamcorper suscipit lobortis</p>
      <p>Lorem ipsum dolor sit amet, consectetuer adipiscing elit, sed diam nonummy nibh euismod tincidunt ut laoreet dolore magna aliquam erat volutpat. Ut wisi edolore te feugait nulla facilisi.</p>
      <p>Lorem ipsum dolor sit amet, cons ectetuer adipiscing elit, sed diam nonummy nibh euismod tinr suscipit lobortis nisl ut aliquip ex ea commodo consequat. Duis autem vel eum iriure dolor in hendrerit in vulputate velit esse molestie consequat, vel illum dolore eu feugiat nulla facilisis at vero eros et accumsan et iusto odio dignissim qui blandit praesent luptatum zzril delenit augue duis dolore te feugait nulla facilisi.<br>Lorem ipsum dolor sit amet, cons ectetuer adipiscing elit, sed diam nonummy nibh euismod tincidunt ut laoreet dolore magna aliquam erat volutpat. Ut wisi enim ad minim veniam, quis nostrud exerci tation ullamcorper suscipit</p>
    </section>

    <div class="footer-rule"></div>
    <footer class="footer-address">
      <div class="web">www.quorvane.com</div>
      <div>Marlowin (IOM) Limited Tavener House Ramsford</div>
      <div>Isle of Man IM98 4QT</div>
    </footer>
  </main>
</body>
</html>
```